KAV cards & more
Business cards, fax cover sheet, letterhead, envelopes, powerpoint slide template
Modern
Tad Willers
Owner
17 Lindgate Row Brookvale, NJ 07950
twkav@mailvane.net
Please integrate my already-completed company logo (attached) in a clean, modern design for business cards, Fax cover sheet, letterhead, envelopes, and powerpoint slide template

```html
<!DOCTYPE html>
<html lang="en">
<head>
<meta charset="utf-8">
<title>KAV Stationery Set</title>
<link rel="stylesheet" href="https://fonts.googleapis.com/css2?family=Montserrat:wght@400;600;800&display=swap">
<style>
:root{
  --green:#5fb12a;
  --green-dark:#2f8a1c;
  --green-light:#b9dc6e;
  --green-pale:#e3f1cf;
  --ink:#2b2b2b;
  --paper:#ffffff;
  --bg:#ffffff;
}
*{margin:0;padding:0;box-sizing:border-box}
html,body{width:1200px;height:540px;overflow:hidden;background:var(--bg);font-family:"Montserrat",sans-serif;color:var(--ink)}
.canvas{position:relative;width:1200px;height:540px}
.sheet{position:absolute;background:var(--paper);box-shadow:0 1px 4px rgba(0,0,0,.25);overflow:hidden}
.sheet svg.waves{position:absolute;inset:0;width:100%;height:100%}
.letterhead{left:31px;top:19px;width:329px;height:504px}
.envelope{left:377px;top:19px;width:386px;height:228px}
.card-front{left:811px;top:19px;width:365px;height:228px}
.sleeve{left:389px;top:271px;width:350px;height:252px;overflow:visible}
.card-back{left:811px;top:283px;width:365px;height:240px}

.brand{position:absolute;display:flex;align-items:center;gap:6px}
.brand-dot{border-radius:50%;background:var(--green)}
.brand-name{font-weight:800;color:var(--green);letter-spacing:1px;line-height:1}
.brand-tag{position:absolute;font-size:6px;color:var(--ink);white-space:nowrap}
.brand-sm .brand-dot{width:18px;height:18px}
.brand-sm .brand-name{font-size:20px}
.brand-lg .brand-dot{width:34px;height:34px}
.brand-lg .brand-name{font-size:40px}
.brand-card .brand-dot{width:58px;height:58px}
.faint-mark{position:absolute;border-radius:50%;background:var(--green-pale);opacity:.8}

.window{position:absolute;left:38px;top:89px;width:125px;height:60px;background:#e6e6e6;border:1px solid #c9c9c9}

.disc{position:absolute;left:196px;top:18px;width:202px;height:202px;border-radius:50%;background:radial-gradient(circle,#fff 0 30%,#f4f4f4 31% 100%);border:1px solid #c8c8c8}
.disc-hub{position:absolute;left:50%;top:50%;width:46px;height:46px;margin:-23px;border-radius:50%;background:var(--green-dark);border:6px solid #9fcf5a}
.disc-hole{position:absolute;left:50%;top:50%;width:14px;height:14px;margin:-7px;border-radius:50%;background:#fff;border:1px solid #aaa}
.disc-mark{position:absolute;left:78px;top:148px;width:44px;height:44px;border-radius:50%;background:var(--green-pale)}

.contact-name{position:absolute;left:122px;top:14px;width:120px;text-align:center;font-size:16px;line-height:1.3}
.contact-block{position:absolute;left:146px;top:72px;font-size:12px;line-height:1.4}
.contact-block .gap{height:8px}
.contact-block .email{font-size:9px}
</style>
</head>
<body>
<main class="canvas">

  <section class="sheet letterhead">
    <svg class="waves" viewBox="0 0 329 504" preserveAspectRatio="none" aria-hidden="true">
      <path d="M0 0H329V8C230 14 120 30 0 52Z" fill="var(--green-light)"/>
      <path d="M0 0H180C120 10 60 22 0 40Z" fill="var(--green)"/>
      <path d="M0 440C110 470 230 470 329 432V504H0Z" fill="var(--green-light)"/>
      <path d="M0 458C110 488 230 486 329 452V504H0Z" fill="var(--green)"/>
      <path d="M0 480C120 504 230 500 329 476V504H0Z" fill="var(--green-dark)"/>
    </svg>
    <div class="brand brand-sm" style="left:14px;top:48px">
      <span class="brand-dot"></span><span class="brand-name">KAV</span>
    </div>
    <p class="brand-tag" style="left:40px;top:70px">Kav Renovations &amp; Upkeep, LLC</p>
    <div class="faint-mark" style="left:200px;top:330px;width:100px;height:100px"></div>
  </section>

  <section class="sheet envelope">
    <svg class="waves" viewBox="0 0 386 228" preserveAspectRatio="none" aria-hidden="true">
      <path d="M0 180C130 200 260 196 386 160V228H0Z" fill="var(--green-light)"/>
      <path d="M0 196C130 214 260 210 386 178V228H0Z" fill="var(--green)"/>
      <path d="M0 214C140 228 260 226 386 200V228H0Z" fill="var(--green-dark)"/>
    </svg>
    <div class="brand brand-sm" style="left:14px;top:22px">
      <span class="brand-dot"></span><span class="brand-name">KAV</span>
    </div>
    <p class="brand-tag" style="left:40px;top:44px">Kav Renovations &amp; Upkeep, LLC</p>
    <div class="window"></div>
    <div class="faint-mark" style="left:240px;top:40px;width:120px;height:120px"></div>
  </section>

  <section class="sheet card-front">
    <svg class="waves" viewBox="0 0 365 228" preserveAspectRatio="none" aria-hidden="true">
      <path d="M0 0H365V10C240 4 110 14 0 40Z" fill="var(--green-light)"/>
      <path d="M0 0H365C230 0 110 6 0 26Z" fill="var(--green)"/>
      <path d="M0 184C130 206 250 200 365 168V228H0Z" fill="var(--green-light)"/>
      <path d="M0 198C130 218 250 214 365 186V228H0Z" fill="var(--green)"/>
      <path d="M0 216C140 228 260 226 365 206V228H0Z" fill="var(--green-dark)"/>
    </svg>
    <div class="brand brand-lg" style="left:50px;top:78px">
      <span class="brand-dot"></span><span class="brand-name">KAV</span>
    </div>
    <p class="brand-tag" style="left:140px;top:126px;font-size:8px">Kav Renovations &amp; Upkeep, LLC</p>
  </section>

  <section class="sheet sleeve">
    <svg class="waves" viewBox="0 0 350 252" preserveAspectRatio="none" aria-hidden="true">
      <path d="M0 0H350V20C220 10 100 24 0 50Z" fill="var(--green-light)"/>
      <path d="M0 0H350C220 0 100 8 0 30Z" fill="var(--green)"/>
      <path d="M0 210C110 230 230 226 350 196V252H0Z" fill="var(--green-light)"/>
      <path d="M0 228C110 246 230 240 350 214V252H0Z" fill="var(--green)"/>
    </svg>
    <div class="brand brand-sm" style="left:14px;top:90px">
      <span class="brand-dot"></span><span class="brand-name">KAV</span>
    </div>
    <p class="brand-tag" style="left:40px;top:112px">Kav Renovations &amp; Upkeep, LLC</p>
    <div class="disc">
      <div class="disc-hub"></div>
      <div class="disc-hole"></div>
      <div class="disc-mark"></div>
    </div>
  </section>

  <section class="sheet card-back">
    <svg class="waves" viewBox="0 0 365 240" preserveAspectRatio="none" aria-hidden="true">
      <path d="M0 196C130 216 250 212 365 184V240H0Z" fill="var(--green-light)"/>
      <path d="M0 210C130 228 250 226 365 200V240H0Z" fill="var(--green)"/>
      <path d="M0 226C140 240 260 238 365 218V240H0Z" fill="var(--green-dark)"/>
    </svg>
    <div class="brand brand-card" style="left:22px;top:40px">
      <span class="brand-dot"></span>
    </div>
    <div class="contact-name">Tad Willers<br>Owner</div>
    <div class="contact-block">
      <p>17 Lindgate Row</p>
      <p>Brookvale, NJ 07950</p>
      <div class="gap"></div>
      <p>Cell&nbsp; 555 014-2290</p>
      <p>Fax&nbsp;&nbsp; 555 014-7731</p>
      <p class="email">Email&nbsp; twkav@mailvane.net</p>
    </div>
  </section>

</main>
</body>
</html>
```